Need updated stationery design for chiropractic clinic

We recently moved our office and are looking to refresh our letterhead, business cards, presentation folder and envelopes. I tend to prefer simple, clean designs. We communicate with a lot of attorneys and want to exude professionalism. I have attached our logo and 2 additional versions (all white and white letters instead of grey).

Target Market(s)

Other medical professionals and attorneys. Business cards will go to patients as well.

Industry/Entity Type

Healthcare

```html
<!DOCTYPE html>
<html lang="en">
<head>
<meta charset="utf-8">
<title>SpineWell Stationery Set</title>
<link rel="stylesheet" href="https://fonts.googleapis.com/css2?family=Montserrat:wght@400;500;600;700&display=swap">
<style>
  :root {
    --bg: #434342;
    --teal: #00cfd2;
    --teal-deep: #00bfc3;
    --blue: #0a93d0;
    --ink: #3a3a3a;
    --muted: #6a6a6a;
    --paper: #ffffff;
    --envelope: #ececec;
  }
  * { box-sizing: border-box; margin: 0; padding: 0; }
  html, body { width: 1028px; height: 1200px; overflow: hidden; }
  body {
    background: var(--bg);
    font-family: "Montserrat", sans-serif;
    color: var(--ink);
    position: relative;
  }
  .sheet { position: absolute; box-shadow: 0 4px 14px rgba(0,0,0,.35); }

  .brand-name {
    font-family: "Montserrat", sans-serif;
    font-weight: 700;
    color: var(--teal);
    display: flex;
    align-items: center;
    gap: 6px;
    line-height: 1;
  }
  .brand-mark { background: var(--blue); display: inline-block; }

  .contact-list { list-style: none; font-size: 7px; line-height: 1.9; }
  .contact-list li { display: flex; align-items: center; gap: 4px; }
  .contact-list svg { width: 8px; height: 8px; flex: none; }

  /* Letterhead */
  .letterhead { left: 40px; top: 60px; width: 460px; height: 650px; background: var(--paper); padding: 34px 30px; }
  .letterhead__top { display: flex; justify-content: space-between; align-items: flex-start; }
  .letterhead .brand-name { font-size: 20px; }
  .letterhead .brand-mark { width: 14px; height: 14px; }
  .recipient { margin-top: 78px; display: flex; justify-content: space-between; align-items: flex-end; }
  .recipient__name { font-size: 14px; font-weight: 600; color: var(--blue); letter-spacing: .3px; margin-bottom: 6px; }
  .recipient__lines { font-size: 7px; line-height: 1.55; color: var(--ink); }
  .recipient__lines p + p { margin-top: 5px; }
  .letter-date { font-size: 7.5px; font-weight: 600; }
  .letter-body { margin-top: 30px; font-size: 6.6px; line-height: 1.5; text-align: justify; color: var(--ink); }
  .letter-body p + p { margin-top: 9px; }
  .sign-off { margin-top: 28px; text-align: right; font-size: 11px; color: var(--ink); }
  .signature { margin: 10px 0 0 auto; width: 80px; height: 36px; background: #ececec; border-radius: 3px; }
  .letterhead__corner { position: absolute; left: 0; bottom: 0; width: 110px; height: 10px; background: var(--blue); }

  /* Folder */
  .folder { left: 528px; top: 60px; width: 460px; height: 650px; background: linear-gradient(160deg, var(--teal) 0%, var(--teal-deep) 100%); color: #fff; }
  .folder__title { position: absolute; right: 40px; top: 390px; text-align: right; }
  .folder__title .brand-name { color: #fff; font-size: 38px; justify-content: flex-end; }
  .folder__title .brand-mark { width: 22px; height: 22px; background: #fff; }
  .folder__url { position: absolute; left: 36px; bottom: 32px; font-size: 13px; font-weight: 500; }

  /* Business cards */
  .card { width: 300px; height: 171px; left: 40px; }
  .card--back { top: 760px; background: var(--paper); padding: 16px 18px; }
  .card--front { top: 955px; background: var(--teal); display: flex; align-items: center; justify-content: center; }
  .card--front .brand-name { color: #fff; font-size: 20px; }
  .card--front .brand-mark { width: 12px; height: 12px; background: #fff; }
  .card__row { display: flex; justify-content: space-between; }
  .card__name { font-size: 10px; font-weight: 600; color: var(--blue); }
  .card__role { font-size: 6px; color: var(--muted); margin-top: 2px; padding-bottom: 3px; border-bottom: 1px solid var(--blue); width: 64px; }
  .card--back .brand-name { font-size: 12px; }
  .card--back .brand-mark { width: 8px; height: 8px; }
  .card--back .contact-list { position: absolute; right: 18px; bottom: 14px; font-size: 6px; text-align: right; }
  .card--back .contact-list li { justify-content: flex-end; }
  .card__stripe { position: absolute; left: 0; bottom: 0; width: 70px; height: 8px; background: var(--teal); }

  /* Envelope */
  .envelope { left: 370px; top: 760px; width: 618px; height: 294px; background: var(--envelope); overflow: hidden; }
  .envelope__flap { position: absolute; left: 0; top: 0; width: 100%; height: 74px; }
  .envelope .brand-name { position: absolute; left: 50%; top: 24px; transform: translateX(-50%); font-size: 22px; }
  .envelope .brand-mark { width: 14px; height: 14px; }
  .envelope__address { position: absolute; right: 20px; bottom: 22px; font-size: 7.5px; text-align: right; line-height: 1.5; color: var(--ink); }
  .envelope__stripe { position: absolute; left: 0; bottom: 0; width: 140px; height: 10px; background: var(--blue); }
</style>
</head>
<body>
  <svg width="0" height="0" style="position:absolute">
    <symbol id="icon-phone" viewBox="0 0 10 10"><rect width="10" height="10" rx="2" fill="#00cfd2"/><path d="M3 2.5c0 2.6 1.9 4.8 4.5 5l.6-1.3-1.3-.7-.6.6C5.4 5.7 4.6 4.9 4.2 4l.6-.6-.7-1.3z" fill="#fff"/></symbol>
    <symbol id="icon-mail" viewBox="0 0 10 10"><rect width="10" height="10" rx="2" fill="#00cfd2"/><rect x="2" y="3" width="6" height="4" fill="none" stroke="#fff" stroke-width=".8"/><path d="M2 3l3 2.2L8 3" fill="none" stroke="#fff" stroke-width=".8"/></symbol>
    <symbol id="icon-web" viewBox="0 0 10 10"><rect width="10" height="10" rx="2" fill="#00cfd2"/><path d="M3.5 2.5l3.8 3-1.6.3 1 1.9-.8.4-1-1.9-1.2 1.1z" fill="#fff"/></symbol>
  </svg>

  <!-- Letterhead -->
  <section class="sheet letterhead">
    <header class="letterhead__top">
      <div class="brand-name"><span class="brand-mark"></span>SpineWell</div>
      <ul class="contact-list">
        <li><svg><use href="#icon-phone"/></svg>0190-555-0142</li>
        <li><svg><use href="#icon-mail"/></svg>hello@spinewellclinic.com</li>
        <li><svg><use href="#icon-web"/></svg>www.spinewellclinic.com</li>
      </ul>
    </header>

    <div class="recipient">
      <div>
        <h2 class="recipient__name">DANA REYES</h2>
        <div class="recipient__lines">
          <p>0190-555-0142</p>
          <p>hello@spinewellclinic.com</p>
          <p>48 Harbor Row, Suite 210<br>Austin, TX 00000</p>
        </div>
      </div>
      <p class="letter-date">12 December, 2023</p>
    </div>

    <div class="letter-body">
      <p>Lorem ipsum dolor sit amet, consectetuer adipiscing elit, sed diam nonummy nibh euismod tincidunt ut laoreet dolore magna aliquam erat volutpat. Ut wisi enim ad minim veniam, quis nostrud exerci tation ullamcorper suscipit lobortis nisl ut aliquip ex ea commodo consequat. Duis autem vel eum iriure dolor in hendrerit in vulputate velit esse molestie consequat, vel illum dolore eu feugiat nulla facilisis at vero eros et accumsan et iusto odio dignissim qui blandit praesent luptatum zzril delenit augue duis dolore te feugait nulla facilisi.</p>
      <p>Lorem ipsum dolor sit amet, cons ectetuer adipiscing elit, sed diam nonummy nibh euismod tincidunt ut laoreet dolore magna aliquam erat volutpat. Ut wisi enim ad minim veniam, quis nostrud exerci tation ullamcorper suscipit lobortis nisl ut aliquip ex ea commodo consequat.<br>Lorem ipsum dolor sit amet, consectetuer adipiscing elit, sed diam nonummy nibh euismod tincidunt ut laoreet dolore magna aliquam erat</p>
      <p>Lorem ipsum dolor sit amet, cons ectetuer adipiscing elit, sed diam nonummy nibh euismod tincidunt ut laoreet dolore magna aliquam erat volutpat. Ut wisi enim ad minim veniam, quis nostrud exerci tation ullamcorper suscipit lobortis nisl ut aliquip ex ea commodo consequat. Lorem ipsum dolor sit amet, consectetuer adipiscing elit, sed diam nonummy nibh euismod tincidunt ut laoreet dolore magna aliquam erat volutpat. Ut wisi enim ad minim veniam, quis nostrud exerci tation ullamcorper suscipit lobortis nisl ut aliquip ex ea commodo consequat. Duis autem vel eum iriure.</p>
    </div>

    <div class="sign-off">
      <p>Managing Director</p>
      <div class="signature" role="img" aria-label="Handwritten signature of the managing director"></div>
    </div>
    <span class="letterhead__corner"></span>
  </section>

  <!-- Presentation folder -->
  <section class="sheet folder">
    <div class="folder__title">
      <div class="brand-name"><span class="brand-mark"></span>SpineWell</div>
    </div>
    <p class="folder__url">www.spinewellclinic.com</p>
  </section>

  <!-- Business card, back -->
  <section class="sheet card card--back">
    <div class="card__row">
      <div>
        <h3 class="card__name">DANA REYES</h3>
        <p class="card__role">Manager</p>
      </div>
      <div class="brand-name"><span class="brand-mark"></span>SpineWell</div>
    </div>
    <ul class="contact-list">
      <li>0190-555-0142<svg><use href="#icon-phone"/></svg></li>
      <li>hello@spinewellclinic.com<svg><use href="#icon-mail"/></svg></li>
      <li>www.spinewellclinic.com<svg><use href="#icon-web"/></svg></li>
    </ul>
    <span class="card__stripe"></span>
  </section>

  <!-- Business card, front -->
  <section class="sheet card card--front">
    <div class="brand-name"><span class="brand-mark"></span>SpineWell</div>
  </section>

  <!-- Envelope -->
  <section class="sheet envelope">
    <svg class="envelope__flap" viewBox="0 0 618 74" preserveAspectRatio="none" aria-hidden="true">
      <path d="M0 0H618L600 52Q594 74 570 74H48Q24 74 18 52Z" fill="#ffffff"/>
    </svg>
    <div class="brand-name"><span class="brand-mark"></span>SpineWell</div>
    <p class="envelope__address">48 Harbor Row, Suite 210<br>Austin, TX 00000</p>
    <span class="envelope__stripe"></span>
  </section>
</body>
</html>
```